realtor require a flyer to market a unit in prime district singapore

This flyer for the sale of "The Valmorelle" is to be distributed to high class district in PRIME homes in singapore. It has to be elegant but eye catching. It must also contain the following detail

1) 1605sqft
2) $2.4 mil with room for negotiation
3) Owner migrating
4) 3 + utility room
5) Desmond Kuah
6) 83527406
7) CEA no. 4718293B

In Singapore the marketing law is pretty strict hence, the following information must also be shown but may be in fine line

1) OKU Homefield network Pte Ltd with LOGO
2) Estate Agency License L5817406M

Target Market(s)

High network owners who has only that 1 sec to to catch their attention

Industry/Entity Type

Marketing

Font styles to use
Serif

Requirements
Must have
• What is stated above
Nice to have
• Nice to have the works and layout nicely crafted out

```html
<!DOCTYPE html>
<html lang="en">
<head>
<meta charset="utf-8">
<title>The Valmorelle – For Sale</title>
<link href="https://fonts.googleapis.com/css2?family=Noto+Sans:ital,wght@0,400;0,600;0,700;1,700&display=swap" rel="stylesheet">
<style>
  :root {
    --brand-navy: #2c2a73;
    --brand-red: #e6262c;
    --ink-black: #000000;
    --paper: #ffffff;
    --page-bg: #ffffff;
    --frame-edge: #d6d6d6;
    --terrace-green: #5d6b4a;
    --terrace-stone: #9a8c73;
    --room-warm: #b9a588;
    --room-light: #e4dfd6;
  }
  * { box-sizing: border-box; margin: 0; padding: 0; }
  html, body {
    width: 1200px; height: 1036px; overflow: hidden;
    background: var(--page-bg);
    font-family: "Noto Sans", sans-serif;
  }
  .canvas { position: relative; width: 1200px; height: 1036px; }

  .flyer {
    position: absolute; left: 71px; top: 49px;
    width: 715px; height: 926px;
    background: var(--paper);
    box-shadow: 0 0 3px rgba(0,0,0,0.35);
    overflow: hidden;
  }

  .hero-photo {
    position: absolute; left: 0; top: 0; width: 715px; height: 380px;
    background:
      radial-gradient(ellipse at 20% 10%, #3f5a33 0%, transparent 45%),
      radial-gradient(ellipse at 85% 20%, #4d6a3c 0%, transparent 40%),
      linear-gradient(180deg, #6f7c63 0%, var(--terrace-green) 40%, var(--terrace-stone) 75%, #8a7a62 100%);
  }

  .agent-tag {
    position: absolute; left: 0; top: 43px; width: 310px; height: 114px;
    background: var(--paper);
    border-radius: 0 14px 14px 0;
  }
  .brand-mark {
    position: absolute; display: flex; align-items: center; gap: 6px;
    color: var(--brand-navy); font-weight: 700;
  }
  .agent-tag .brand-mark { left: 50px; top: 36px; font-size: 30px; }
  .brand-mark .brand-square { width: 16px; height: 16px; background: var(--brand-red); }
  .agent-tag .agent-details {
    position: absolute; left: 155px; top: 19px;
    font-size: 13.5px; line-height: 16.5px; color: var(--brand-navy);
  }

  .feature-band {
    position: absolute; left: 0; top: 380px; width: 715px; height: 228px;
    background: var(--brand-navy);
  }

  .room-thumb {
    position: absolute; top: 294px; width: 150px; height: 150px;
    border-radius: 50%; border: 11px solid var(--paper); overflow: hidden;
  }
  .room-thumb .room-photo { width: 100%; height: 100%; }
  .room-thumb.living { left: 171px; }
  .room-thumb.living .room-photo { background: linear-gradient(180deg, var(--room-light) 0%, #cfc6b5 50%, #6b5a48 100%); }
  .room-thumb.bedroom { left: 346px; }
  .room-thumb.bedroom .room-photo { background: linear-gradient(90deg, #a8a39c 0%, var(--room-light) 45%, var(--room-warm) 100%); }
  .room-thumb.dining { left: 521px; }
  .room-thumb.dining .room-photo { background: linear-gradient(180deg, #d8d1c4 0%, var(--room-warm) 55%, #3b352f 100%); }

  .listing-title {
    position: absolute; left: 43px; top: 490px; color: var(--paper);
  }
  .listing-title .property-name { font-size: 27px; font-weight: 600; line-height: 30px; letter-spacing: 0.3px; }
  .listing-title .sale-label { font-size: 46px; font-weight: 600; line-height: 48px; }

  .listing-facts {
    position: absolute; left: 323px; top: 484px;
    list-style: none; color: var(--paper);
    font-size: 19px; line-height: 24px;
  }
  .listing-facts li::before { content: "•"; margin-right: 8px; }

  .tagline-band {
    position: absolute; left: 0; top: 608px; width: 715px; height: 72px;
    background: var(--ink-black);
    display: flex; align-items: center; justify-content: center;
  }
  .tagline {
    color: var(--paper); font-size: 31px; font-weight: 700; font-style: italic; letter-spacing: 0.4px;
  }

  .footer-brand { left: 55px; top: 800px; font-size: 48px; }
  .footer-brand .brand-square { width: 22px; height: 22px; }

  .agent-card {
    position: absolute; left: 352px; top: 710px; width: 363px; height: 175px;
    background: var(--brand-navy);
    border-radius: 12px 0 0 12px;
  }
  .agent-portrait {
    position: absolute; left: 28px; top: 27px; width: 118px; height: 118px;
    border-radius: 50%; background: linear-gradient(180deg, #f2f2f2 0%, #dcdcdc 60%, #2a2a2a 100%);
  }
  .agent-card .agent-details {
    position: absolute; left: 170px; top: 37px;
    color: var(--paper); font-size: 16px; line-height: 19.7px;
  }
</style>
</head>
<body>
<div class="canvas">
  <article class="flyer">
    <div class="hero-photo" role="img" aria-label="Photo of the leafy garden terrace with a white dining table and chairs"></div>

    <div class="agent-tag">
      <div class="brand-mark"><span class="brand-square"></span>OKU</div>
      <p class="agent-details">Desmond Kuah<br>83527406<br>CEA no. 4718293B<br>Estate Agency License<br>L5817406M</p>
    </div>

    <section class="feature-band"></section>

    <div class="room-thumb living"><div class="room-photo" role="img" aria-label="Photo of the bright living room"></div></div>
    <div class="room-thumb bedroom"><div class="room-photo" role="img" aria-label="Photo of the bedroom"></div></div>
    <div class="room-thumb dining"><div class="room-photo" role="img" aria-label="Photo of the dining area"></div></div>

    <h1 class="listing-title">
      <span class="property-name">THE VALMORELLE</span><br>
      <span class="sale-label">FOR SALE</span>
    </h1>

    <ul class="listing-facts">
      <li>1605 sq ft</li>
      <li>$2.4 mil with room for negotiation</li>
      <li>Owner migrating</li>
      <li>3 + utility room</li>
    </ul>

    <div class="tagline-band"><p class="tagline">Elegant Home with Excellent View</p></div>

    <div class="brand-mark footer-brand"><span class="brand-square"></span>OKU</div>

    <aside class="agent-card">
      <div class="agent-portrait" role="img" aria-label="Portrait photo of agent Desmond Kuah"></div>
      <p class="agent-details">Desmond Kuah<br>83527406<br>CEA no. 4718293B<br>Estate Agency<br>License L5817406M</p>
    </aside>
  </article>
</div>
</body>
</html>
```